Dozing Heron

Need a business card for our restaurant. Restaurant and Bar in the mountains of North Idaho. Rustic looking card

Contact Information for Business Card

rustic design, wood and metal looking, primarily neutral colors

Requirements
Must have
• Name, address, phone number, website, email address

```html
<!DOCTYPE html>
<html lang="en">
<head>
<meta charset="utf-8">
<title>Dozing Heron – Business Card</title>
<link href="https://fonts.googleapis.com/css2?family=Lato:wght@400;700&display=swap" rel="stylesheet">
<style>
  :root {
    --backdrop: #3a3a3a;
    --card: #1c1c1c;
    --card-panel: #232323;
    --pattern-dark: #161616;
    --pattern-light: #2c2c2c;
    --ink: #f2f2f2;
    --ink-soft: #d6d6d6;
    --rule: #bdbdbd;
  }
  * { box-sizing: border-box; margin: 0; padding: 0; }
  html, body { width: 1200px; height: 694px; overflow: hidden; }
  body {
    background: var(--backdrop);
    font-family: "Lato", sans-serif;
    color: var(--ink);
    position: relative;
  }
  .card {
    position: absolute;
    top: 192px;
    width: 540px;
    height: 310px;
    border-radius: 22px;
    background: var(--card);
    overflow: hidden;
  }
  .card--front { left: 40px; }
  .card--back { left: 620px; }

  .front-pattern {
    position: absolute;
    inset: 0;
    background: linear-gradient(135deg, var(--pattern-dark) 0%, var(--pattern-light) 55%, var(--pattern-dark) 100%);
  }
  .front-name {
    position: absolute;
    left: 0; right: 0;
    top: 140px;
    text-align: center;
    font-weight: 700;
    font-size: 22px;
    letter-spacing: 1px;
    color: var(--ink);
  }

  .back-panel {
    position: absolute;
    left: 18px;
    top: 118px;
    right: 0;
    bottom: 0;
    border-radius: 20px 0 22px 20px;
    background: var(--card-panel);
  }
  .brand {
    position: absolute;
    right: 30px;
    top: 38px;
    display: flex;
    align-items: center;
    gap: 10px;
    font-weight: 700;
    font-size: 22px;
    color: var(--ink);
  }
  .brand__dot {
    width: 14px; height: 14px;
    border-radius: 50%;
    background: var(--ink);
  }
  .rule {
    position: absolute;
    height: 1px;
    background: var(--rule);
  }
  .rule--top { left: 230px; right: 30px; top: 100px; }
  .rule--name { left: 40px; width: 220px; top: 222px; }

  .person { position: absolute; left: 40px; top: 162px; }
  .person__name { font-weight: 700; font-size: 24px; color: var(--ink); }
  .person__role { font-size: 15px; color: var(--ink-soft); margin-top: 2px; }

  .contacts {
    position: absolute;
    left: 40px;
    top: 232px;
    list-style: none;
    font-size: 15px;
    color: var(--ink);
  }
  .contacts li { display: flex; align-items: center; gap: 10px; height: 22px; }
  .contacts svg { width: 14px; height: 14px; fill: var(--ink); }

  .address {
    position: absolute;
    right: 30px;
    top: 124px;
    text-align: right;
    font-size: 15px;
    line-height: 1.45;
    color: var(--ink);
  }
</style>
</head>
<body>
  <section class="card card--front">
    <div class="front-pattern" role="img" aria-label="Embossed tonal repeat pattern of the restaurant emblem"></div>
    <p class="front-name">Dozing Heron</p>
  </section>

  <section class="card card--back">
    <div class="back-panel"></div>
    <div class="brand"><span class="brand__dot"></span>Dozing Heron</div>
    <div class="rule rule--top"></div>

    <div class="address">
      <p>421, Address line goes here</p>
      <p>45452, Country name</p>
    </div>

    <div class="person">
      <p class="person__name">Daniel Harper</p>
      <p class="person__role">Owner</p>
    </div>
    <div class="rule rule--name"></div>

    <ul class="contacts">
      <li>
        <svg viewBox="0 0 16 16" aria-hidden="true"><path d="M3.6 1.5l2.3 2.4-1.3 1.8c.9 2 2.4 3.5 4.4 4.4l1.8-1.3 2.4 2.3-1.4 2.4C6.6 13.3 2.7 9.4 1.2 3.2z"/></svg>
        123.456.7890
      </li>
      <li>
        <svg viewBox="0 0 16 16" aria-hidden="true"><path d="M1 3h14v1.2L8 9 1 4.2z"/><path d="M1 5.6l7 4.8 7-4.8V13H1z"/></svg>
        info@webname.com
      </li>
      <li>
        <svg viewBox="0 0 16 16" aria-hidden="true"><path d="M8 1a7 7 0 100 14A7 7 0 008 1zm0 1.5c.8 0 1.7 1.5 2 3.7H6c.3-2.2 1.2-3.7 2-3.7zM2.6 7.3h2.3c0 .5 0 .9.1 1.4H2.6a5.6 5.6 0 010-1.4zm3.4 0h4c0 .5 0 .9-.1 1.4H6.1C6 8.2 6 7.8 6 7.3zm5.1 0h2.3a5.6 5.6 0 010 1.4H11c.1-.5.1-.9.1-1.4zM6 9.8h4c-.3 2.2-1.2 3.7-2 3.7s-1.7-1.5-2-3.7z"/></svg>
        www.website.com
      </li>
    </ul>
  </section>
</body>
</html>
```